Lantern Hill Publicity is a new boutique Press Office with a small roster of well-chosen clients across an array of disciplines; from Art and Technology to Restaurants and Fashion. Based in Greenpoint Brooklyn, Lantern Hill Publicity achieves outstanding results through hard work, tenacity, efficiency and a sense of humor. We need a simple, versatile and classic design. We would like each side of the card to be white text on a black background.

Boutique

```html
<!DOCTYPE html>
<html lang="en">
<head>
<meta charset="utf-8">
<title>Lantern Hill Publicity — Business Card</title>
<link rel="stylesheet" href="https://fonts.googleapis.com/css2?family=Arimo:wght@400;700&display=swap">
<style>
  :root {
    --backdrop: #2b2826;
    --card-black: #141414;
    --card-edge: #1c1c1c;
    --ink-white: #f4f4f4;
    --ink-soft: #d9d9d9;
    --gloss: #3b3b3b;
    --gloss-light: #4a4a4a;
  }
  * { margin: 0; padding: 0; box-sizing: border-box; }
  html, body {
    width: 1200px; height: 864px; overflow: hidden;
    background: var(--backdrop);
    font-family: "Arimo", Arial, sans-serif;
  }
  .canvas { position: relative; width: 1200px; height: 864px; }
  .card {
    position: absolute; width: 540px; height: 309px;
    background: var(--card-black);
    border: 1px solid var(--card-edge);
    box-shadow: 0 18px 40px rgba(0,0,0,.45);
  }
  .card--front { left: 50px; top: 140px; }
  .card--back { left: 610px; top: 415px; }

  /* Front side: tone-on-tone gloss */
  .front-brand {
    position: absolute; left: 0; right: 0; top: 112px;
    text-align: center; color: var(--gloss-light);
    font-size: 26px; font-weight: 400; letter-spacing: 5px; text-transform: uppercase;
  }
  .front-web {
    position: absolute; left: 0; right: 0; top: 196px;
    text-align: center; color: var(--gloss);
    font-size: 13px; letter-spacing: 4px;
  }

  /* Back side */
  .back-brand {
    position: absolute; left: 34px; top: 120px; width: 250px;
    text-align: center; color: var(--ink-white);
    font-size: 19px; font-weight: 400; letter-spacing: 3px; text-transform: uppercase; line-height: 1.5;
  }
  .divider {
    position: absolute; left: 304px; top: 40px; width: 1px; height: 230px;
    background: linear-gradient(to bottom, transparent, #cfcfcf 30%, #cfcfcf 70%, transparent);
  }
  .contact { position: absolute; left: 324px; top: 58px; color: var(--ink-white); }
  .contact__name { font-size: 18px; font-weight: 700; }
  .contact__title { font-size: 14px; margin-bottom: 14px; color: var(--ink-soft); }
  .contact__address { font-size: 12.5px; line-height: 1.4; margin-bottom: 10px; }
  .contact__list { list-style: none; font-size: 12.5px; }
  .contact__list li { display: flex; align-items: center; gap: 9px; height: 19px; }
  .contact__list svg { width: 12px; height: 12px; fill: var(--ink-white); flex: none; }
</style>
</head>
<body>
<main class="canvas">
  <section class="card card--front" aria-label="Card front">
    <p class="front-brand">Lantern Hill Publicity</p>
    <p class="front-web">www.lanternhillpr.com</p>
  </section>

  <section class="card card--back" aria-label="Card back">
    <p class="back-brand">Lantern Hill<br>Publicity</p>
    <div class="divider"></div>
    <div class="contact">
      <p class="contact__name">Jordan Vale</p>
      <p class="contact__title">President</p>
      <p class="contact__address">2417 Harbor Lane<br>Brookfield, NY 11020</p>
      <ul class="contact__list">
        <li><svg viewBox="0 0 12 12"><path d="M1 4 Q6 0 11 4 L10 6 8 5 8 4 Q6 3 4 4 L4 5 2 6Z M2 7 H10 V11 H2Z"/></svg>555 0142 2253</li>
        <li><svg viewBox="0 0 12 12"><path d="M3 0 H9 V12 H3Z M4 1.5 V9 H8 V1.5Z"/></svg>555 0187 5335</li>
        <li><svg viewBox="0 0 12 12"><path d="M3 0 H9 V4 H3Z M1 4 H11 V11 H1Z M3 6 H9 V7 H3Z"/></svg>555 0163 3856</li>
        <li><svg viewBox="0 0 12 12"><path d="M0 2 H12 V10 H0Z M1 3 L6 7 11 3" stroke="#141414" stroke-width="1"/></svg>jordan@lanternhillpr.com</li>
        <li><svg viewBox="0 0 12 12"><circle cx="6" cy="6" r="6"/><path d="M0 6 H12 M6 0 V12" stroke="#141414" stroke-width="1"/></svg>www.lanternhillpr.com</li>
      </ul>
    </div>
  </section>
</main>
</body>
</html>
```